Looking for a new business card design

We are looking for a corporate looking yet still a bit different then the rest. I would like the card black with the picture on the back and the phrase "Lighting the way to goal ZERO" on the back as well. Then a clean look on the front with a bit of an edge.

Target Market(s)

Corporate oil executives and drilling supervisors

Industry/Entity Type

Oil And Gas

Contact Information for Business Card

Black, bold, clean lines.

Font styles to use
Sans Serif

Requirements
Must have
• Picture on the back with the slogan "Lighting the way to goal ZERO"
• Black background
• Stands out

```html
<!DOCTYPE html>
<html lang="en">
<head>
<meta charset="utf-8">
<title>Vestra Energy – Business Card</title>
<link href="https://fonts.googleapis.com/css2?family=Open+Sans:wght@400;600;700;800&display=swap" rel="stylesheet">
<style>
  :root {
    --stage: #2b2b2b;
    --card-black: #050607;
    --card-white: #ffffff;
    --brand-blue: #356a9b;
    --brand-lime: #b5c724;
    --ink: #3a3a3a;
    --photo-dark: #0d1410;
    --photo-mid: #4a4a38;
    --photo-light: #b8b39a;
  }
  * { box-sizing: border-box; margin: 0; padding: 0; }
  html, body {
    width: 1200px; height: 950px; overflow: hidden;
    background: var(--stage);
    font-family: "Open Sans", Arial, sans-serif;
  }
  .sheet {
    width: 1200px; height: 950px;
    display: flex; flex-direction: column; align-items: center; justify-content: center;
    gap: 40px;
  }
  .card {
    position: relative; width: 720px; height: 411px; overflow: hidden;
    box-shadow: 0 12px 30px rgba(0,0,0,.5);
  }

  /* Back side */
  .card--back { background: var(--card-black); }
  .site-photo {
    position: absolute; left: 60px; top: 40px; width: 600px; height: 300px;
    border-radius: 50%;
    background: radial-gradient(ellipse at 45% 45%, var(--photo-light) 0%, var(--photo-mid) 40%, var(--photo-dark) 70%, var(--card-black) 100%);
  }
  .back-brand {
    position: absolute; left: 360px; top: 258px;
    display: flex; align-items: center; gap: 8px;
    color: var(--brand-lime); font-weight: 800; font-size: 20px; letter-spacing: .5px;
  }
  .back-brand .mark { width: 14px; height: 14px; border-radius: 50%; background: var(--brand-lime); }
  .slogan {
    position: absolute; left: 0; right: 0; top: 300px; text-align: center;
    color: #fff; font-weight: 700; font-size: 27px; letter-spacing: .3px;
    text-shadow: 0 2px 6px rgba(0,0,0,.8);
  }

  /* Front side */
  .card--front { background: var(--card-white); }
  .card-art { position: absolute; inset: 0; }
  .holder { position: absolute; left: 36px; top: 176px; color: #fff; }
  .holder-name { font-weight: 700; font-size: 22px; letter-spacing: .5px; white-space: nowrap; }
  .holder-title { font-size: 15px; margin-top: 2px; }

  .brand {
    position: absolute; left: 412px; top: 104px;
    display: flex; align-items: center; gap: 10px;
  }
  .brand .mark { width: 34px; height: 34px; border-radius: 50%; background: var(--brand-blue); flex: none; }
  .brand-name { color: var(--brand-lime); font-weight: 800; font-size: 30px; letter-spacing: .5px; white-space: nowrap; }

  .divider { position: absolute; left: 500px; top: 178px; width: 1px; height: 108px; background: var(--ink); }

  .address {
    position: absolute; right: 234px; top: 236px; text-align: right;
    color: var(--ink); font-size: 14px; line-height: 20px; white-space: nowrap;
  }
  .website {
    position: absolute; right: 234px; top: 284px;
    color: var(--brand-blue); font-weight: 700; font-size: 13px; letter-spacing: 1px; white-space: nowrap;
  }

  .contacts { position: absolute; right: 16px; top: 174px; list-style: none; }
  .contacts li {
    display: flex; align-items: center; justify-content: flex-end; gap: 8px;
    color: var(--ink); font-size: 14px; line-height: 24px; white-space: nowrap;
  }
  .contacts svg { width: 15px; height: 15px; fill: var(--brand-blue); flex: none; }
</style>
</head>
<body>
<main class="sheet">

  <section class="card card--back">
    <div class="site-photo" role="img" aria-label="Night aerial photograph of a floodlit drilling rig site"></div>
    <div class="back-brand"><span class="mark"></span>VESTRA</div>
    <p class="slogan">Lighting the way to goal ZERO</p>
  </section>

  <section class="card card--front">
    <svg class="card-art" viewBox="0 0 720 411" aria-hidden="true">
      <rect x="0" y="0" width="720" height="262" fill="var(--brand-blue)"/>
      <ellipse cx="560" cy="300" rx="330" ry="290" fill="var(--brand-lime)"/>
      <ellipse cx="590" cy="320" rx="300" ry="285" fill="var(--card-white)"/>
    </svg>

    <div class="holder">
      <p class="holder-name">MARA LINDQVIST</p>
      <p class="holder-title">President</p>
    </div>

    <div class="brand"><span class="mark"></span><span class="brand-name">Vestra Energy</span></div>

    <div class="divider"></div>

    <p class="address">412 Harbor Ridge Road<br>Millbrook, NY 12545</p>
    <p class="website">www.vestraenergy.com</p>

    <ul class="contacts">
      <li>555 0142 7781
        <svg viewBox="0 0 24 24"><path d="M6.6 10.8a15 15 0 0 0 6.6 6.6l2.2-2.2c.3-.3.7-.4 1-.2 1.1.4 2.3.6 3.6.6.6 0 1 .4 1 1V20c0 .6-.4 1-1 1A17 17 0 0 1 3 4c0-.6.4-1 1-1h3.5c.6 0 1 .4 1 1 0 1.3.2 2.5.6 3.6.1.3 0 .7-.2 1z"/></svg>
      </li>
      <li>555 0187 3409
        <svg viewBox="0 0 24 24"><path d="M7 1h10a2 2 0 0 1 2 2v18a2 2 0 0 1-2 2H7a2 2 0 0 1-2-2V3a2 2 0 0 1 2-2zm0 3v14h10V4zm5 15.5a1 1 0 1 0 0 2 1 1 0 0 0 0-2z"/></svg>
      </li>
      <li>555 0163 9025
        <svg viewBox="0 0 24 24"><path d="M6 2h10v5H6zM3 8h18a1 1 0 0 1 1 1v9a1 1 0 0 1-1 1h-3v3H6v-3H3a1 1 0 0 1-1-1V9a1 1 0 0 1 1-1zm5 8v4h8v-4z"/></svg>
      </li>
      <li>mara@vestraenergy.com
        <svg viewBox="0 0 24 24"><path d="M2 5h20v14H2zm2 2v.5l8 5 8-5V7zm0 3v7h16v-7l-8 5z"/></svg>
      </li>
    </ul>
  </section>

</main>
</body>
</html>
```